martial arts school needs a flyer to attract new starters in wing chun kung fu

we need a flyer design to be sent out in the local community to attract new customers to our martial arts school. we intend to run introduction classes for begineers. the design should be attractive to new starters looking to get fit - learn a martial art - make new friends - improve self confidence.
also the flyer should say "free class with this flyer" . we also need big poster to put up around the local area

the following dress should be on the design Aire Valley Martial ArtsGround FloorThe MillGreengage RoadKeighleyBD21 5LH Added Sunday, April 5, 2015

contact telephone number on the design ; 079 64820 557 Added Sunday, April 5, 2015

• it must say - wing chun kung fu classes - introduction classes -

```html
<!DOCTYPE html>
<html lang="en">
<head>
<meta charset="utf-8">
<title>Wing Chun Kung Fu Classes</title>
<link href="https://fonts.googleapis.com/css2?family=Montserrat:wght@400;600;700&family=Rubik+Dirt&display=swap" rel="stylesheet">
<style>
  :root {
    --bg-dark: #161616;
    --bg-mid: #2e2e2e;
    --gold: #d6c326;
    --white: #ffffff;
    --photo-dark: #2a2a2a;
    --photo-light: #d9d6d0;
  }
  html, body {
    margin: 0;
    padding: 0;
    overflow: hidden;
    background: var(--bg-dark);
  }
  .flyer {
    position: relative;
    width: 849px;
    height: 1200px;
    overflow: hidden;
    background: radial-gradient(ellipse at 45% 40%, var(--bg-mid) 0%, #232323 45%, var(--bg-dark) 100%);
    font-family: "Montserrat", Arial, sans-serif;
    color: var(--white);
  }
  .hero-photo {
    position: absolute;
    left: 440px;
    top: 0;
    width: 409px;
    height: 1200px;
    background: linear-gradient(100deg, rgba(42,42,42,0) 0%, var(--photo-dark) 18%, #6b6a68 45%, var(--photo-light) 75%, #bdb9b2 100%);
  }
  .headline, .offer-title {
    position: absolute;
    margin: 0;
    font-family: "Rubik Dirt", Impact, sans-serif;
    font-weight: 400;
    text-transform: uppercase;
    color: var(--white);
    letter-spacing: 1px;
  }
  .headline {
    left: 34px;
    top: 34px;
    font-size: 90px;
    line-height: 96px;
    transform: rotate(-2deg);
    transform-origin: left top;
  }
  .intro-panel {
    position: absolute;
    left: 77px;
    top: 431px;
    width: 344px;
    height: 465px;
    border: 2px solid var(--gold);
    border-top: none;
    box-sizing: border-box;
    text-align: center;
  }
  .intro-panel::before,
  .intro-panel::after {
    content: "";
    position: absolute;
    top: 0;
    width: 16px;
    height: 2px;
    background: var(--gold);
  }
  .intro-panel::before { left: -2px; }
  .intro-panel::after { right: -2px; }
  .intro-title {
    position: absolute;
    left: -20px;
    right: -20px;
    top: -44px;
    margin: 0;
    font-size: 40px;
    line-height: 46px;
    font-weight: 700;
    color: var(--gold);
  }
  .address-note {
    margin: 74px 0 0;
    font-size: 18px;
    line-height: 25px;
    font-weight: 400;
  }
  .address-line {
    margin: 14px 0 0;
    font-size: 17px;
    line-height: 24px;
    font-weight: 700;
  }
  .date-gold {
    margin: 10px 0 0;
    font-size: 23px;
    line-height: 30px;
    font-weight: 700;
    color: var(--gold);
  }
  .contact-label {
    margin: 28px 0 0;
    font-size: 18px;
    line-height: 24px;
  }
  .phone {
    margin: 4px 0 0;
    font-size: 24px;
    line-height: 30px;
    font-weight: 700;
    color: var(--gold);
    letter-spacing: 0.5px;
  }
  .date-white {
    margin: 2px 0 0;
    font-size: 17px;
    line-height: 25px;
    font-weight: 700;
  }
  .offer-title {
    left: 74px;
    top: 955px;
    font-size: 72px;
    line-height: 80px;
    transform: rotate(-2deg);
    transform-origin: left top;
  }
  .offer-line {
    position: absolute;
    margin: 0;
    font-weight: 700;
    color: var(--gold);
    text-align: center;
  }
  .offer-with {
    left: 180px;
    top: 1032px;
    width: 140px;
    font-size: 42px;
    line-height: 50px;
  }
  .offer-flyer {
    left: 130px;
    top: 1086px;
    width: 250px;
    font-size: 44px;
    line-height: 52px;
  }
</style>
</head>
<body>
<main class="flyer">
  <div class="hero-photo" role="img" aria-label="Photo of a martial artist in a white uniform and black belt holding an open-palm guard"></div>

  <h1 class="headline">Wing Chun<br>Kung Fu<br>Classes</h1>

  <section class="intro-panel">
    <h2 class="intro-title">Introduction<br>Classes</h2>
    <p class="address-note">The Following Dress should<br>be on the Design Brook Hollow<br>Martial Arts Ground Floor</p>
    <p class="address-line">The Tanneryspindlewick<br>Roadmarrowbytq47 9Rx</p>
    <p class="date-gold">Added Sunday,<br>April 5, 2015</p>
    <p class="contact-label">Contact Information:</p>
    <p class="phone">079 64820 557</p>
    <p class="date-white">Added Sunday,<br>April 5, 2015</p>
  </section>

  <h2 class="offer-title">Free Class</h2>
  <p class="offer-line offer-with">with</p>
  <p class="offer-line offer-flyer">This Flyer</p>
</main>
</body>
</html>
```